Velmora Trade Hall (front page)

We need a design of a front page for our Velmora Trade Hall website (vth.co.uk). Our company is based in the United Kingdom and offers investors from all over the world an opportunity to invest into bitcoin and litecoin.

We have been developing this cutting edge technology for past 2 years based on our in depth knowledge on conventional stock and currency trading technology and methodology. We have run many test against penetration, security and stability and now are ready to deploy.

Recent news about vulnerability of such platforms leave a great deal of unease from retail investors about investing into cryptocurrency. We are set to challenge this attitude. Our background is payments in particular regulated environment in the UK. We are keen to apply our wealth of experience to provide secure and reliable trading platform and advance cryptocurrency as means of legal tender.

The front page should be based on the feel and look of our current technology vth.co.uk. Some of you have already been involved in logo design for our company, please see the attached mockups. The page should have this minimalist design, very clean and light.

Seek inspiration form www.korvelin.net, www.trusmarq.com, vip.plomwerth.com and other bitcoin exchanges.

We look forward to receiving your ideas.

You can also refer to our social pages:
https://www.facebook.com/vth.co.uk
https://twitter.com/vth_uk

We would like you to focus your efforts at designing the page in such a way so that it is very easy for visitor be open an account with the exchange. We must focus at informing the visitor about the bitcoin, how to my buy, how to sell, look at the general overview of the maker and CONVERTING him/her sing up. This is the most important!!

Regards,
Oren

Reason: Dear all, We are very keen on getting this design done right the first time. The key success is conversion of visitors to subscribers and then to traders. It is absolutely essential make the registration process as streamlined as possible! When we are calling them to act by "Change the world one bitcoin at a time" we should give them a opportunity to provide us with relevant account creation details: email, password, confirm password. Please visit quenzo.co.uk for ideas. Secondly, tell them what is a bitcoin, why a bitcoin is a good investment and how to invest. Finally, it is important to inform visitors of "who we are", what sets us apart from other exchanges, tell them about our experience. In our view graphs and live order books are important but they might turn some visitors away especially the ones that are not accustomed to online trading. Think of what would you like to see on the page if you wanted YOURSELF to invest. What would make you to create an account and use it? Think what will work, we are here to revolutionise how people do business.... any wild ideas put them to us. OUR BUDGET JUST GONE UP!!!

Target Market(s)

A combination of professional and consumer bitcoin investors.

Requirements
Must have
• News section

```html
<!DOCTYPE html>
<html lang="en">
<head>
<meta charset="utf-8">
<title>Velmora Trade Hall</title>
<link href="https://fonts.googleapis.com/css2?family=Open+Sans:wght@400;600;700&family=Michroma&family=Great+Vibes&display=swap" rel="stylesheet">
<style>
:root{
  --blue:#0f9bd7;
  --blue-dark:#0b84b8;
  --ink:#333;
  --muted:#555;
  --grey:#ececec;
  --panel:#f5f5f5;
  --orange:#f7931a;
  --footer:#4b4b4d;
}
*{margin:0;padding:0;box-sizing:border-box}
html,body{width:823px;height:1200px;overflow:hidden}
body{font-family:'Open Sans',sans-serif;color:var(--ink);background:#fff;position:relative}
.abs{position:absolute}

.header{left:0;top:0;width:823px;height:97px;background:#fff}
.brand{left:53px;top:24px;display:flex;align-items:center;gap:12px}
.brand-dot{width:18px;height:18px;border-radius:50%;background:var(--blue);flex:none}
.brand-name{font-size:15px;font-weight:600;color:#333;letter-spacing:3px;line-height:24px}
.divider{left:223px;top:8px;width:1px;height:80px;background:#555}
.tagline{left:310px;top:22px;font-family:'Great Vibes',cursive;font-size:34px;color:var(--blue)}

.nav{left:0;top:97px;width:823px;height:47px;background:var(--blue)}
.nav ul{list-style:none;display:flex;position:absolute;left:53px;top:14px;gap:18px}
.nav li{font-family:'Michroma',sans-serif;font-size:14px;color:#fff;letter-spacing:1px}
.nav li.active{color:#444;position:relative}
.nav li.active::after{content:"";position:absolute;left:6px;top:21px;width:32px;height:6px;
  background:radial-gradient(circle,transparent 1.6px,#444 2px,#444 3px,transparent 3.2px) 0 0/11px 6px repeat-x}
.search{left:770px;top:97px;width:16px;height:47px;background:#444}

.stage{left:0;top:144px;width:823px;height:411px;background:var(--grey)}
.slider{left:37px;top:159px;width:749px;height:380px;overflow:hidden;
  box-shadow:0 2px 6px rgba(0,0,0,.25)}
.slide-photo{position:absolute;inset:0;background:linear-gradient(180deg,#e9eef3 0%,#c7d0d8 55%,#7c858c 100%)}
.slide-title{left:0;width:749px;top:10px;text-align:center;font-size:23px;font-weight:700;color:#666}
.screen{left:270px;top:50px;width:320px;height:212px;background:#1c1d20;border-radius:3px}
.screen-inner{position:absolute;left:12px;top:10px;width:296px;height:192px;background:#e6ecf1}
.ticks{list-style:none;position:absolute;left:14px;top:10px}
.ticks li{font-size:15px;color:#222;margin-bottom:7px;display:flex;align-items:center;gap:6px}
.cta{left:336px;top:198px;background:var(--orange);color:#fff;font-size:12px;font-weight:600;padding:4px 9px;border-radius:2px;transform:rotate(-3deg)}
.login{left:462px;top:226px;font-size:11px;color:#555}
.coin{left:626px;top:32px;width:104px;height:104px;border-radius:50%;background:var(--orange);border:4px solid #f5a740;box-shadow:0 2px 4px rgba(0,0,0,.3)}
.arrow{top:151px;width:45px;height:45px;border-radius:50%}
.arrow.prev{left:9px;background:#666}
.arrow.next{left:696px;background:var(--blue)}

.feature{top:555px;width:244px;height:196px;background:var(--panel);text-align:center}
.feature.on{background:var(--blue);color:#fff}
.feature .icon{margin:14px auto 0;width:88px;height:88px;border-radius:50%;background:var(--blue);display:flex;align-items:center;justify-content:center}
.feature.on .icon{background:#fff}
.feature h3{font-size:15px;font-weight:700;margin-top:10px;color:#444}
.feature.on h3{color:#fff}
.feature p{font-size:11px;line-height:15px;padding:2px 12px;color:var(--muted)}
.feature.on p{color:#fff}
.band{left:0;top:751px;width:823px;height:270px;background:#efefef}

.section-title{font-size:15px;font-weight:600;color:#333}
.post{left:53px;width:431px;height:70px;border-bottom:1px solid #d6d6d6}
.cal{position:absolute;left:0;top:4px;width:38px;height:40px;background:#fff;border-radius:4px;box-shadow:0 1px 2px rgba(0,0,0,.3);text-align:center}
.cal .m{font-size:9px;color:#333;display:block;margin-top:3px}
.cal .d{font-size:17px;font-weight:700;font-style:italic;color:#222;line-height:17px}
.cal.hot .m,.cal.hot .d{color:var(--blue)}
.post h4{position:absolute;left:45px;top:0;font-size:12px;font-weight:600;color:#222}
.post h4.hot{color:var(--blue)}
.post p{position:absolute;left:45px;top:18px;font-size:10.5px;line-height:15px;color:var(--muted);white-space:nowrap}
.btn{background:var(--blue);color:#fff;font-size:10px;padding:4px 7px;border-radius:2px}

.video{left:546px;top:793px;width:240px;height:150px;background:linear-gradient(135deg,#0d4655,#0b3540)}
.video-title{left:0;width:240px;top:82px;text-align:center;color:#fff;font-size:14px;font-weight:700;line-height:15px}
.play{left:105px;top:51px;width:30px;height:22px;background:#e52d27;border-radius:5px}
.player{left:0;bottom:0;width:240px;height:26px;background:#1b1b1b;font-size:7px;color:#ccc}
.input{left:546px;top:985px;width:148px;height:21px;border:1px solid #ccc;background:#fff;font-size:10px;color:#444;padding:3px 6px}
.sub{left:709px;top:985px;width:77px;height:21px;background:var(--blue);color:#fff;font-size:10px;text-align:center;line-height:21px}

.foot-brand{left:37px;top:1040px;width:110px;text-align:center}
.foot-brand .dot{width:18px;height:18px;border-radius:50%;background:var(--blue);margin:0 auto 10px}
.foot-brand .rule{width:56px;height:1px;background:#888;margin:0 auto 10px}
.foot-brand span{font-size:12px;font-weight:600;color:#333;letter-spacing:1px;line-height:17px}
.col h5{font-size:15px;font-weight:700;color:var(--blue);margin-bottom:9px}
.col a{display:block;font-size:10px;color:#333;text-decoration:none;line-height:16.5px}
.col a.on{color:var(--blue)}
.follow{left:566px;top:1039px;font-size:15px;font-weight:700;color:var(--blue)}
.social{top:1077px;width:24px;height:24px;border-radius:50%;background:#444}
.social.fb{background:#3b5d96}
.copyright{left:0;top:1156px;width:823px;height:44px;background:var(--footer);color:#bbb;font-size:10px;text-align:center;line-height:44px}
</style>
</head>
<body>
<header class="abs header">
  <div class="abs brand"><span class="brand-dot"></span><span class="brand-name">Velmora<br>Trade Hall</span></div>
  <div class="abs divider"></div>
  <div class="abs tagline">Change the world one bitcoin at a time</div>
</header>
<nav class="abs nav">
  <ul><li class="active">Home</li><li>Security</li><li>How it works</li><li>Features</li><li>Support</li><li>Contact</li></ul>
</nav>
<div class="abs search"><svg width="16" height="47" viewBox="0 0 16 47"><circle cx="7" cy="22" r="3.2" fill="none" stroke="#fff" stroke-width="1.6"/><line x1="9.3" y1="24.3" x2="12" y2="27" stroke="#fff" stroke-width="1.8"/></svg></div>

<section class="abs stage"></section>
<section class="abs slider">
  <div class="slide-photo" role="img" aria-label="Photo of three colleagues at a meeting table in a bright office"></div>
  <div class="abs slide-title">Trade Bitcoin, Litecoin conventional stock and more...</div>
  <div class="abs screen"><div class="screen-inner">
    <ul class="ticks">
      <li><svg width="12" height="10"><path d="M1 5l3.5 3.5L11 1" fill="none" stroke="#1d8fd0" stroke-width="2"/></svg>Consectetur Adipiscing elit</li>
      <li><svg width="12" height="10"><path d="M1 5l3.5 3.5L11 1" fill="none" stroke="#1d8fd0" stroke-width="2"/></svg>Nulla eufringilla magna</li>
      <li><svg width="12" height="10"><path d="M1 5l3.5 3.5L11 1" fill="none" stroke="#1d8fd0" stroke-width="2"/></svg>Felis cOngue tristique</li>
      <li><svg width="12" height="10"><path d="M1 5l3.5 3.5L11 1" fill="none" stroke="#1d8fd0" stroke-width="2"/></svg>Phasellus neque mialiquam</li>
    </ul>
  </div></div>
  <div class="abs cta">Open An Account</div>
  <div class="abs login">Login to your account</div>
  <div class="abs coin"></div>
  <div class="abs arrow prev"><svg width="45" height="45"><path d="M30 22.5H15M21 16l-6.5 6.5L21 29" fill="none" stroke="#fff" stroke-width="2.5"/></svg></div>
  <div class="abs arrow next"><svg width="45" height="45"><path d="M15 22.5h15M24 16l6.5 6.5L24 29" fill="none" stroke="#fff" stroke-width="2.5"/></svg></div>
</section>

<div class="abs band"></div>
<article class="abs feature on" style="left:37px">
  <div class="icon"><svg width="60" height="60"><circle cx="30" cy="30" r="27" fill="var(--blue)"/><path d="M30 14v16l12 4" fill="none" stroke="#fff" stroke-width="5"/></svg></div>
  <h3>Penetration</h3>
  <p>Lorem ipsum dolor sit amet, consectetur adipiscing elit. Sed a tempus ipsum. In eu libero id lacus</p>
</article>
<article class="abs feature" style="left:290px">
  <div class="icon"><svg width="60" height="60"><circle cx="30" cy="30" r="27" fill="#fff"/><circle cx="30" cy="30" r="18" fill="var(--blue)" opacity=".35"/></svg></div>
  <h3>Stability</h3>
  <p>Lorem ipsum dolor sit amet, consectetur adipiscing elit. Sed a tempus ipsum. In eu libero id lacus</p>
</article>
<article class="abs feature" style="left:542px">
  <div class="icon"><svg width="60" height="66"><path d="M30 4a21 21 0 0 1 21 21c0 15-21 37-21 37S9 40 9 25A21 21 0 0 1 30 4z" fill="#fff"/><circle cx="30" cy="24" r="8" fill="var(--blue)"/></svg></div>
  <h3>Security</h3>
  <p>Lorem ipsum dolor sit amet, consectetur adipiscing elit. Sed a tempus ipsum. In eu libero id lacus</p>
</article>

<h2 class="abs section-title" style="left:52px;top:762px">Latest Blog Posts</h2>
<div class="abs post" style="top:792px"><div class="cal hot"><span class="m">MAR</span><span class="d">20</span></div><h4 class="hot">Lorem ipsum dolor sit amet,</h4><p>Donec nec dignissim lorem. Vestibu lum lesuada ac auctor vitae, mollis tempus<br>Donec nec dignissim lorem. Vestibu lum lesuada ac auctor vitae, mollis tempus</p></div>
<div class="abs post" style="top:862px"><div class="cal"><span class="m">MAR</span><span class="d">25</span></div><h4>Lorem ipsum dolor sit amet,</h4><p>Donec nec dignissim lorem. Vestibu lum lesuada ac auctor vitae, mollis tempus<br>Donec nec dignissim lorem. Vestibu lum lesuada ac auctor vitae, mollis tempus</p></div>
<div class="abs post" style="top:932px;border:0"><div class="cal"><span class="m">MAR</span><span class="d">26</span></div><h4>Lorem ipsum dolor sit amet,</h4><p>Donec nec dignissim lorem. Vestibu lum lesuada ac auctor vitae, mollis tempus<br>Donec nec dignissim lorem. Vestibu lum lesuada ac auctor vitae, mollis tempus</p></div>
<div class="abs btn" style="left:426px;top:986px">View All</div>

<h2 class="abs section-title" style="left:545px;top:762px">Video</h2>
<div class="abs video" role="img" aria-label="Explainer video still with market ticker backdrop">
  <div class="abs play"></div>
  <div class="abs video-title">Biticon and Liticon<br>How It work?</div>
  <div class="abs player"><div style="height:3px;background:#555"></div><span style="position:absolute;left:60px;top:10px">0:00 / 3:22</span></div>
</div>
<h2 class="abs section-title" style="left:546px;top:962px">Subcribe To Our Mailing List</h2>
<div class="abs input">Enter Email Address</div>
<div class="abs sub">Subscribe</div>

<div class="abs foot-brand"><div class="dot"></div><div class="rule"></div><span>Velmora<br>Trade Hall</span></div>
<div class="abs col" style="left:198px;top:1039px"><h5>Menu</h5><a class="on" href="#">Home</a><a href="#">Security</a><a href="#">How it work</a><a href="#">Features</a><a href="#">Contact</a></div>
<div class="abs col" style="left:307px;top:1039px"><h5>Help</h5><a href="#">What is bitcoin?</a><a href="#">How to buy bitcoins?</a><a href="#">How to sell bitcoins?</a><a href="#">FAQ</a></div>
<div class="abs col" style="left:454px;top:1039px"><h5>Data</h5><a href="#">Overview</a><a href="#">Order Book</a><a href="#">API</a></div>
<div class="abs follow">Follow Velmora Trade Hall</div>
<div class="abs social fb" style="left:620px"></div>
<div class="abs social" style="left:652px"></div>
<div class="abs social" style="left:684px"></div>
<div class="abs social" style="left:715px"></div>
<footer class="abs copyright">Copyright © 2014 velmora trade hall. All Rights Reserved</footer>
</body>
</html>
```